Renewable energy website needs a wordpress website

We are a Renewable Energy company specialising in Energy Management, LED Lights and Solar PV Systems based in Kuala Lumpur.
We need wordpress website designed to match our company identity.
We would like to stick with similar shades of blue & green as our logo and to keep it fresh and creative at the same time.

It Company

```html
<!DOCTYPE html>
<html lang="en">
<head>
<meta charset="utf-8">
<title>Verdanta Power</title>
<link rel="stylesheet" href="https://fonts.googleapis.com/css2?family=Raleway:wght@200;300;400&family=Open+Sans:wght@400;600;700&family=Oswald:wght@400&display=swap">
<style>
:root{
  --black:#000;
  --green:#8dc63f;
  --green-dark:#5f9a34;
  --blue:#1fa8e0;
  --blue-link:#29abe2;
  --grey-band:#555555;
  --grey-text:#555;
  --white:#fff;
  --light:#e4e4e4;
}
*{margin:0;padding:0;box-sizing:border-box}
html,body{width:1200px;height:2493px;overflow:hidden}
body{position:relative;background:var(--white);font-family:"Open Sans",Arial,sans-serif}
.abs{position:absolute}

/* header */
.site-header{left:0;top:0;width:1200px;height:156px;background:var(--black)}
.brand{left:58px;top:58px;display:flex;align-items:center;gap:12px}
.brand-dot{width:46px;height:46px;border-radius:50%;border:5px solid var(--blue)}
.brand-name{font-family:"Raleway",sans-serif;font-weight:400;font-size:22px;color:var(--blue);letter-spacing:1px}
.main-nav{left:607px;top:0;height:140px;display:flex}
.main-nav a{display:flex;align-items:center;height:140px;padding:0 18px;color:var(--blue-link);text-decoration:none;font-family:Arial,sans-serif;font-size:17px}
.main-nav a.current{background:var(--green);color:var(--white);padding:0 15px}

/* hero */
.hero{left:0;top:156px;width:1200px;height:555px;background:linear-gradient(180deg,#2f62a8 0%,#6f9acf 45%,#c9d3de 65%,#8a939c 100%)}
.hero-title{left:58px;top:216px;font-family:"Raleway",sans-serif;font-weight:300;font-size:54px;color:var(--white)}
.hero-btn{left:435px;top:304px;width:185px;height:48px;background:var(--green);display:flex;align-items:center;gap:12px;padding-left:12px;font-family:"Raleway",sans-serif;font-size:27px;color:var(--white)}

/* services */
.service{top:800px;width:380px}
.service-icon{width:100px;height:100px;border-radius:50%;background:var(--green-dark);position:absolute;left:0;top:0;display:flex;align-items:center;justify-content:center}
.service-title{position:absolute;left:117px;top:0;font-family:"Raleway",sans-serif;font-weight:300;font-size:35px;line-height:37px}
.service-title .g{color:var(--green)}
.service-title .b{color:var(--blue)}
.service-text{position:absolute;left:0;top:138px;width:330px;font-family:Arial,sans-serif;font-size:16.5px;line-height:21.5px;color:var(--grey-text)}
.more-btn{position:absolute;left:-2px;top:282px;width:158px;height:43px;display:flex}
.more-btn .label{width:116px;background:var(--blue);color:var(--white);font-family:Arial,sans-serif;font-weight:bold;font-size:20px;display:flex;align-items:center;justify-content:center}
.more-btn .go{flex:1;background:var(--green);display:flex;align-items:center;justify-content:center}

/* about band */
.about-band{left:0;top:1225px;width:1200px;height:761px;background:var(--grey-band)}
.notch-label{font-family:"Open Sans",sans-serif;font-size:14px;text-align:center;width:160px}
.welcome-title{left:23px;top:1320px;font-family:"Raleway",sans-serif;font-weight:300;font-size:41px;line-height:43px;color:var(--white)}
.welcome-photo{left:23px;top:1429px;width:530px;height:366px;background:linear-gradient(180deg,#1b59c0 0%,#5aa6e6 55%,#3b6fb3 78%,#4a8a2a 100%)}
.welcome-text{left:23px;top:1817px;width:540px;font-family:"Open Sans",sans-serif;font-size:16.5px;line-height:20px;color:var(--light)}
.blog-title{left:628px;top:1322px;font-family:"Raleway",sans-serif;font-weight:300;font-size:41px;color:var(--white)}
.post{width:270px;height:140px}
.post-date{position:absolute;left:0;top:0;width:100px;height:108px;background:var(--green-dark);color:var(--white);text-align:center}
.post-date::after{content:"";position:absolute;right:-14px;top:14px;border-left:14px solid var(--green-dark);border-top:11px solid transparent;border-bottom:11px solid transparent}
.post-day{font-family:"Oswald",sans-serif;font-size:44px;line-height:48px;padding-top:12px;display:block}
.post-month{font-family:Arial,sans-serif;font-size:16px;display:block}
.post-head{position:absolute;left:116px;top:-1px;width:150px;font-family:Arial,sans-serif;font-size:14.5px;line-height:17px;color:var(--blue-link)}
.post-text{position:absolute;left:116px;top:40px;width:140px;font-family:Arial,sans-serif;font-size:14.5px;line-height:17.5px;color:#cfcfcf}

/* connect */
.connect-band{left:0;top:1986px;width:1200px;height:507px;background:var(--blue)}
.footer-brand{left:27px;top:2102px;display:flex;align-items:center;gap:10px}
.footer-brand .brand-dot{border-color:var(--white);background:none}
.footer-brand .brand-name{color:var(--white)}
.footer-text{left:27px;top:2183px;width:320px;font-family:Arial,sans-serif;font-size:16.5px;line-height:21px;color:var(--white)}
.footer-copy{left:27px;top:2288px;font-family:Arial,sans-serif;font-size:16.5px;color:var(--white)}
.contact-form{left:396px;top:2101px;width:379px}
.field{width:379px;height:36px;background:var(--white);margin-bottom:7px;padding:7px 12px;font-family:Arial,sans-serif;font-size:13.5px;color:#3a8fc7}
.field.message{height:138px}
.submit-btn{margin-top:13px;width:157px;height:54px;background:var(--white);display:flex;align-items:center;gap:10px;padding-left:12px;font-family:"Open Sans",sans-serif;font-weight:700;font-size:22px;color:var(--blue)}
.social{left:844px;top:2100px;display:flex;gap:17px}
.social span{width:53px;height:53px;border-radius:50%;background:var(--white)}
.company{left:844px;top:2173px;font-family:Arial,sans-serif;color:var(--white);font-size:16.5px;line-height:21px}
.company strong{font-size:20px;display:block;margin-bottom:3px}
</style>
</head>
<body>

<header class="abs site-header">
  <div class="abs brand"><span class="brand-dot"></span><span class="brand-name">VERDANTA POWER</span></div>
  <nav class="abs main-nav">
    <a class="current">Home</a><a>About</a><a>Products</a><a>Services</a><a>Blog</a><a>Find Us</a>
  </nav>
</header>

<section class="abs hero" role="img" aria-label="Photo of a technician in a hard hat installing a solar panel on a roof under a blue sky"></section>
<h1 class="abs hero-title">A Better Source of Energy</h1>
<div class="abs hero-btn">
  <svg width="30" height="30" viewBox="0 0 30 30"><circle cx="15" cy="15" r="14" fill="#fff"/><path d="M8 15h12M15 9l6 6-6 6" stroke="#8dc63f" stroke-width="3.5" fill="none"/></svg>
  read more
</div>

<!-- services -->
<div class="abs service" style="left:27px">
  <div class="service-icon"><svg width="60" height="60" viewBox="0 0 60 60"><circle cx="30" cy="30" r="26" fill="none" stroke="#fff" stroke-width="4"/><path d="M4 30h52M30 4c-12 14-12 38 0 52M30 4c12 14 12 38 0 52" fill="none" stroke="#fff" stroke-width="3"/></svg></div>
  <h2 class="service-title"><span class="g">ENERGY</span><br><span class="b">MANAGEMENT</span></h2>
  <p class="service-text">Lorem ipsum dolor sit amet, consectetur adipisicing elit, sed do eiusmod tempor incididunt ut lare et dolore magna aliqua. Ut enim ad minim veniam, quis nostrud exercitation ullamco massa astom.</p>
  <div class="more-btn"><span class="label">more</span><span class="go"><svg width="16" height="18"><path d="M1 1l14 8-14 8z" fill="#fff"/></svg></span></div>
</div>
<div class="abs service" style="left:422px">
  <div class="service-icon"><svg width="60" height="64" viewBox="0 0 60 64"><circle cx="30" cy="24" r="18" fill="none" stroke="#fff" stroke-width="4"/><rect x="21" y="44" width="18" height="6" fill="#fff"/><rect x="22" y="52" width="16" height="5" fill="#fff"/><rect x="26" y="58" width="8" height="4" fill="#fff"/></svg></div>
  <h2 class="service-title"><span class="g">LED</span><br><span class="b">LIGHTS</span></h2>
  <p class="service-text">Ut telloribus eget elemetum vel curleif end elit. Aean auctoetnaliir pis nteerutru Nulla fn nec ero ante ipsummis fauulet utrice posere cubtsed leo pharetu nec augue.</p>
  <div class="more-btn"><span class="label">more</span><span class="go"><svg width="16" height="18"><path d="M1 1l14 8-14 8z" fill="#fff"/></svg></span></div>
</div>
<div class="abs service" style="left:818px">
  <div class="service-icon"><svg width="66" height="60" viewBox="0 0 66 60"><path d="M8 6h50l6 28H2z" fill="none" stroke="#fff" stroke-width="3.5"/><path d="M24 6l-3 28M42 6l3 28M5 20h56" stroke="#fff" stroke-width="3"/><rect x="30" y="34" width="6" height="18" fill="#fff"/><rect x="20" y="52" width="26" height="4" fill="#fff"/></svg></div>
  <h2 class="service-title"><span class="g">SOLAR</span><br><span class="b">PV SYSTEMS</span></h2>
  <p class="service-text">Lorem ipsum dolor sit amet, consectetur adipisicing elit, sed do eiusmod tempor incididunt ut lare et dolore magna aliqua. Ut enim ad minim veniam, quis nostrud exercitation ullamco massa astom.</p>
  <div class="more-btn"><span class="label">more</span><span class="go"><svg width="16" height="18"><path d="M1 1l14 8-14 8z" fill="#fff"/></svg></span></div>
</div>

<!-- about & blog -->
<section class="abs about-band"></section>
<svg class="abs" style="left:520px;top:1225px" width="160" height="56" viewBox="0 0 160 56"><path d="M0 0h160L80 56z" fill="#fff"/></svg>
<div class="abs notch-label" style="left:520px;top:1230px;color:#555">ABOUT</div>

<h2 class="abs welcome-title">Welcome to Verdanta Power</h2>
<div class="abs welcome-photo" role="img" aria-label="Illustration of solar panels on green grass beneath a bright blue sky with white clouds"></div>
<p class="abs welcome-text">Ut telloribus eget elemetum vel curleif end elit. Aean auctoetnaliir pis nteerutruNulla fn nec ero ante ipsummis fauulet utrice posere cubtsed leo pharetu nec augue. Naelit magnrerit siaiverra sed nullanec portadiam eu massaneclus non era acinia fermentum. Donec in velit vel ipsum auctorulvinarroin ullamc.</p>

<h2 class="abs blog-title">BLOG</h2>
<article class="abs post" style="left:625px;top:1429px"><div class="post-date"><span class="post-day">12</span><span class="post-month">NOV</span></div><h3 class="post-head">LOREM IPSUM DOLOR AMET</h3><p class="post-text">Psum dolor sit amet, consectetuer adipiscing elit, sed diam nonummy nibh euismod .</p></article>
<article class="abs post" style="left:912px;top:1429px"><div class="post-date"><span class="post-day">04</span><span class="post-month">NOV</span></div><h3 class="post-head">LOREM IPSUM DOLOR AMET</h3><p class="post-text">Psum dolor sit amet, consectetuer adipiscing elit, sed diam nonummy nibh euismod .</p></article>
<article class="abs post" style="left:625px;top:1611px"><div class="post-date"><span class="post-day">27</span><span class="post-month">OCT</span></div><h3 class="post-head">LOREM IPSUM DOLOR AMET</h3><p class="post-text">Psum dolor sit amet, consectetuer adipiscing elit, sed diam nonummy nibh euismod .</p></article>
<article class="abs post" style="left:912px;top:1611px"><div class="post-date"><span class="post-day">15</span><span class="post-month">OCT</span></div><h3 class="post-head">LOREM IPSUM DOLOR AMET</h3><p class="post-text">Psum dolor sit amet, consectetuer adipiscing elit, sed diam nonummy nibh euismod .</p></article>
<article class="abs post" style="left:625px;top:1795px"><div class="post-date"><span class="post-day">27</span><span class="post-month">OCT</span></div><h3 class="post-head">LOREM IPSUM DOLOR AMET</h3><p class="post-text">Psum dolor sit amet, consectetuer adipiscing elit, sed diam nonummy nibh euismod .</p></article>
<article class="abs post" style="left:912px;top:1795px"><div class="post-date"><span class="post-day">15</span><span class="post-month">OCT</span></div><h3 class="post-head">LOREM IPSUM DOLOR AMET</h3><p class="post-text">Psum dolor sit amet, consectetuer adipiscing elit, sed diam nonummy nibh euismod .</p></article>

<!-- connect -->
<footer class="abs connect-band"></footer>
<svg class="abs" style="left:520px;top:1986px" width="160" height="56" viewBox="0 0 160 56"><path d="M0 0h160L80 56z" fill="#555"/></svg>
<div class="abs notch-label" style="left:520px;top:1990px;color:var(--blue)">CONNECT</div>

<div class="abs footer-brand"><span class="brand-dot"></span><span class="brand-name">VERDANTA POWER</span></div>
<p class="abs footer-text">Ut telloribus eget elemetum vel curleif end elit. Aean auctoetnaliir pis nteerutru Nulla fn nec ero ante ipsummis fauulet utrice posere cubtsed leo pharetu nec .</p>
<p class="abs footer-copy">© 2013 • Privacy Policy</p>

<form class="abs contact-form">
  <div class="field">Name</div>
  <div class="field">Email</div>
  <div class="field">Company</div>
  <div class="field message">Message</div>
  <div class="submit-btn"><svg width="30" height="30" viewBox="0 0 30 30"><circle cx="15" cy="15" r="14" fill="#1fa8e0"/><path d="M8 15h12M15 9l6 6-6 6" stroke="#fff" stroke-width="3.5" fill="none"/></svg>SUBMIT</div>
</form>

<div class="abs social" aria-label="Social links"><span></span><span></span><span></span><span></span><span></span></div>
<address class="abs company" style="font-style:normal"><strong>Verdanta Power</strong>42 Harlow Lane<br>Northfield, NF2 7QT.<br>Phone: +1 555 010 2468</address>

</body>
</html>
```